Refreshed PPT Presentation for US based firms

There are basically 4 types of slides in this presentation:
* Roadmap (Title, Agenda, Billboards)
* Teaching (Content, Examples)
* Samples (Real life samples)
* Polls (Placeholders for interactive polls)
We want new templates for each of these types of templates with coordinated graphics, images, icons and fonts.

```html
<!DOCTYPE html>
<html lang="en">
<head>
<meta charset="utf-8">
<title>Advice And Counsel Through Email – Slide Deck</title>
<link href="https://fonts.googleapis.com/css2?family=Abril+Fatface&family=Montserrat:wght@400;500;600;700&display=swap" rel="stylesheet">
<style>
:root{
  --navy:#1d4556;
  --teal:#117a7b;
  --coral:#f26b6b;
  --paper:#ffffff;
  --ground:#d7d8da;
  --ink:#1d4556;
  --muted:#7b8a91;
  --soft:#c9d5da;
}
*{box-sizing:border-box;margin:0;padding:0}
html,body{width:1050px;height:1200px;overflow:hidden}
body{background:var(--ground);font-family:"Montserrat",sans-serif;color:var(--ink)}
.deck{position:absolute;left:36px;top:26px;display:grid;grid-template-columns:repeat(3,321px);grid-auto-rows:180px;gap:10px 8px}
.slide{position:relative;background:var(--paper);overflow:hidden;box-shadow:0 3px 6px rgba(0,0,0,.18)}
.abs{position:absolute}
.side{position:absolute;left:0;top:0;bottom:0;width:107px;background:var(--navy)}
.title{position:absolute;left:21px;top:14px;font-family:"Abril Fatface",serif;font-size:12.5px;line-height:1.05;color:var(--navy);font-weight:400}
.title.light{color:#fff}
.title::before{content:"";position:absolute;left:-21px;top:5px;width:17px;height:4px;border-top:1px solid var(--coral);border-bottom:1px solid var(--coral)}
.url{position:absolute;right:8px;top:7px;font-size:4.6px;letter-spacing:.2px;color:var(--navy)}
.pg{position:absolute;right:8px;bottom:6px;font-size:5.5px;font-weight:600;color:var(--navy)}
.tiny{font-size:4px;line-height:1.3;color:var(--muted)}
.tiny.light{color:var(--soft)}
.small{font-size:4.6px;line-height:1.3;color:var(--muted)}
.head{font-size:5.6px;font-weight:500;color:var(--navy)}
.head.teal{color:var(--teal)}
.num{font-family:"Abril Fatface",serif;font-size:12px;color:var(--navy);line-height:1}
.photo{position:absolute;background:linear-gradient(135deg,#7e8c94,#c9cfd2 55%,#59666e)}
.ring{position:absolute;border-radius:50%;border:5px solid var(--coral)}
.chip{position:absolute;background:var(--coral)}
.ico{position:absolute;width:24px;height:24px;border-radius:50%;background:var(--navy);display:flex;align-items:center;justify-content:center}
.centre{text-align:center}
svg text{font-family:"Montserrat",sans-serif}
</style>
</head>
<body>
<main class="deck">

<!-- 1 cover -->
<section class="slide">
  <div class="abs" style="left:221px;top:0;width:100px;height:180px;background:var(--navy)"></div>
  <div class="abs" style="left:10px;top:23px;width:1px;height:78px;background:var(--navy)"></div>
  <div class="abs" style="left:10px;top:120px;width:1px;height:68px;background:var(--navy)"></div>
  <h1 class="abs" style="left:23px;top:22px;font-family:'Abril Fatface',serif;font-weight:400;font-size:16px;line-height:1.22;color:var(--navy)">Advice And<br>Counsel Throug<br>Email</h1>
  <p class="abs" style="left:19px;top:117px;font-size:6.2px;font-weight:600;color:var(--coral)">Mara Reyes</p>
  <p class="abs" style="left:19px;top:126px;font-size:6.2px;font-weight:600;color:var(--navy)">for Northgate Legal P.C.</p>
  <p class="abs" style="left:19px;top:148px;font-size:5.2px;color:var(--navy)">Go to www.pollspace.com/<span style="color:var(--coral)">marareyes</span></p>
  <div class="photo" role="img" aria-label="Colleagues talking around a meeting table" style="left:162px;top:21px;width:137px;height:138px"></div>
  <div class="ring" style="left:147px;top:144px;width:28px;height:28px"></div>
</section>

<!-- 2 contents -->
<section class="slide">
  <div class="side"></div>
  <h2 class="title light">Contents.</h2>
  <p class="abs tiny light" style="left:21px;top:112px;width:72px">Lorem ipsum dolor sit amet, consectetuer adipiscing elit, sed diam nonummy nibh euismod tincid</p>
  <span class="url">www.pollspace.com/marareyes</span>
  <div class="abs" style="left:135px;top:24px;width:170px">
    <div style="display:flex;gap:4px;margin-bottom:15px"><span class="num">1.</span><div><p class="head">Lorem ipsum</p><p class="tiny">Lorem ipsum dolor sit amet, consectetur adipiscing elit, sed do eiusmod tempor incididunt ut labore et dolore magna aliqua.</p></div></div>
    <div style="display:flex;gap:4px;margin-bottom:15px"><span class="num">2.</span><div><p class="head">Lorem ipsum</p><p class="tiny">Lorem ipsum dolor sit amet, consectetuer adipiscing elit, sed diam nonummy nibh euismod tincid</p></div></div>
    <div style="display:flex;gap:4px;margin-bottom:15px"><span class="num">3.</span><div><p class="head">Lorem ipsum</p><p class="tiny">Lorem ipsum dolor sit amet, consectetuer adipiscing elit, sed diam nonummy nibh euismod tincid</p></div></div>
    <div style="display:flex;gap:4px"><span class="num">4.</span><div><p class="head">Lorem ipsum</p><p class="tiny">Lorem ipsum dolor sit amet, consectetuer adipiscing elit, sed diam nonummy nibh euismod tincid</p></div></div>
  </div>
  <span class="pg">02</span>
</section>

<!-- 3 agenda -->
<section class="slide">
  <div class="side"></div>
  <h2 class="title light">Agenda.</h2>
  <p class="abs tiny light" style="left:21px;top:112px;width:72px">Lorem ipsum dolor sit amet, consectetuer adipiscing elit, sed diam nonummy nibh euismod tincid</p>
  <span class="url">www.pollspace.com/marareyes</span>
  <div class="ico" style="left:149px;top:25px"><svg width="11" height="11" viewBox="0 0 11 11"><rect x="2" y="1" width="7" height="9" fill="none" stroke="#fff"/><path d="M3.5 4h4M3.5 6h4M3.5 8h2.5" stroke="#fff" stroke-width=".8"/></svg></div>
  <div class="ico" style="left:229px;top:25px"><svg width="11" height="11" viewBox="0 0 11 11"><path d="M1 10h9" stroke="#fff"/><rect x="2" y="6" width="1.6" height="3.5" fill="#fff"/><rect x="5" y="4" width="1.6" height="5.5" fill="#fff"/><rect x="8" y="2" width="1.6" height="7.5" fill="#fff"/></svg></div>
  <div class="ico" style="left:149px;top:101px"><svg width="11" height="11" viewBox="0 0 11 11"><path d="M1 1.5h9v6H4l-2.5 2v-2H1z" fill="none" stroke="#fff"/><path d="M3 3.8h5M3 5.6h4" stroke="#fff" stroke-width=".7"/></svg></div>
  <div class="ico" style="left:229px;top:101px"><svg width="11" height="11" viewBox="0 0 11 11"><path d="M3 1h5v3a2.5 2.5 0 0 1-5 0z" fill="#fff"/><path d="M5.5 6.5v2M3.5 10h4" stroke="#fff"/><path d="M3 2H1.3a1.7 1.7 0 0 0 1.7 2.2M8 2h1.7A1.7 1.7 0 0 1 8 4.2" fill="none" stroke="#fff" stroke-width=".7"/></svg></div>
  <div class="abs centre" style="left:126px;top:53px;width:70px"><p class="head teal">Lorem ipsum</p><p class="tiny">Lorem ipsum dolor sit amet, consectetuer adipiscing elit, sed diam nonummy nibh euismod tincidunt ut</p></div>
  <div class="abs centre" style="left:206px;top:53px;width:70px"><p class="head teal">Lorem ipsum</p><p class="tiny">Lorem ipsum dolor sit amet, consectetuer adipiscing elit, sed diam nonummy nibh euismod</p></div>
  <div class="abs centre" style="left:126px;top:126px;width:70px"><p class="head teal">Lorem ipsum</p><p class="tiny">unt ut dolore magna aliquam erat volutpat. Ut wisi enim ad minim veniam</p></div>
  <div class="abs centre" style="left:206px;top:126px;width:70px"><p class="head teal">Lorem ipsum</p><p class="tiny">nibh euismod tincidunt ut dolore magna aliquam erat volutpat. Ut wisi enim ad minim veniam</p></div>
  <span class="pg">03</span>
</section>

<!-- 4 about -->
<section class="slide">
  <div class="side"></div>
  <h2 class="title light">About Us.</h2>
  <p class="abs tiny light" style="left:21px;top:112px;width:72px">Lorem ipsum dolor sit amet, consectetuer adipiscing elit, sed diam nonummy nibh euismod tincid</p>
  <span class="url">www.pollspace.com/marareyes</span>
  <p class="abs small" style="left:115px;top:32px;width:64px;font-size:4.5px">Lorem ipsum dolor sit amet, consectetuer adipiscing elit, sed diam nonummy nibh euismod tincidunt ut laoreet dolore magna aliquam erat volutpat. Ut wisi enim ad minim veniam, quis nostrud exerci tation ullamcorper suscipit lobortis nisl ut aliquip ex ea commodo consequat. Duis autem vel eum iriure dolor in hendrerit in vulputate velit esse molestie consequat, vel</p>
  <div class="photo" role="img" aria-label="Business team working on laptops at a meeting table" style="left:192px;top:26px;width:116px;height:126px"></div>
  <div class="ring" style="left:181px;top:142px;width:24px;height:24px"></div>
  <span class="pg">04</span>
</section>

<!-- 5 education -->
<section class="slide">
  <h2 class="title">Our Education.</h2>
  <span class="url">www.pollspace.com/marareyes</span>
  <div class="abs" style="left:25px;top:33px;width:269px;height:129px;background:var(--navy)"></div>
  <div class="abs" style="left:63px;top:46px;width:53px;height:80px;border:1px solid var(--teal);border-radius:6px;padding:13px 3px 0" >
    <svg width="8" height="9" viewBox="0 0 8 9" style="display:block;margin:0 auto"><circle cx="4" cy="3.5" r="3" fill="none" stroke="#f26b6b" stroke-width=".8"/><path d="M3 7.5h2M3.3 8.6h1.4" stroke="#f26b6b" stroke-width=".7"/></svg>
    <p class="centre" style="font-size:4.6px;font-weight:700;color:var(--coral);margin:2px 0">IDEA</p>
    <p class="tiny light centre" style="font-size:3.2px">Lorem ipsum dolor sit amet, consectetuer adipiscing elit, sed diam nonummy nibh euismod tincidunt ut laoreet dolore magna aliquam erat volutpat. Ut wisi enim ad minim veniam, quis nostrud exerci tation ullamcorper suscipit lobortis nisl ut aliquip ex ea commodo</p>
  </div>
  <div class="abs" style="left:133px;top:46px;width:53px;height:80px;border:1px solid var(--teal);border-radius:6px;padding:13px 3px 0">
    <svg width="9" height="8" viewBox="0 0 9 8" style="display:block;margin:0 auto"><rect x=".5" y="1" width="8" height="6" fill="none" stroke="#f26b6b" stroke-width=".8"/><path d="M.5 1l4 3.2 4-3.2" fill="none" stroke="#f26b6b" stroke-width=".8"/></svg>
    <p class="centre" style="font-size:4.6px;font-weight:700;color:var(--coral);margin:2px 0">PROMOTION</p>
    <p class="tiny light centre" style="font-size:3.2px">Lorem ipsum dolor sit amet, consectetuer adipiscing elit, sed diam nonummy nibh euismod tincidunt ut laoreet dolore magna aliquam erat volutpat. Ut wisi enim ad minim veniam, quis nostrud exerci tation ullamcorper suscipit lobortis nisl ut aliquip ex ea commodo</p>
  </div>
  <div class="abs" style="left:204px;top:46px;width:53px;height:80px;border:1px solid var(--teal);border-radius:6px;padding:13px 3px 0">
    <svg width="9" height="8" viewBox="0 0 9 8" style="display:block;margin:0 auto"><path d="M1 .5v7h7.5M2.5 5.5l5-4M5 1.5h2.5v2.5" fill="none" stroke="#f26b6b" stroke-width=".8"/></svg>
    <p class="centre" style="font-size:4.6px;font-weight:700;color:var(--coral);margin:2px 0">GROWTH</p>
    <p class="tiny light centre" style="font-size:3.2px">Lorem ipsum dolor sit amet, consectetuer adipiscing elit, sed diam nonummy nibh euismod tincidunt ut laoreet dolore magna aliquam erat volutpat. Ut wisi enim ad minim veniam, quis nostrud exerci tation ullamcorper suscipit lobortis nisl ut aliquip ex ea commodo</p>
  </div>
  <p class="abs centre" style="left:40px;top:137px;width:240px;font-size:3.6px;line-height:1.3;color:#fff">Lorem ipsum dolor sit amet, consectetuer adipiscing elit, sed diam nonummy nibh euismod tincidunt ut laoreet dolore magna aliquam erat volutpat. Ut wisi enim ad minim veniam, quis nostrud exerci tation ullamcorper suscipit lobortis nisl ut aliquip ex ea commodo consequat. Duis autem vel eum iriure dolor in hendrerit</p>
  <span class="pg">05</span>
</section>

<!-- 6 advice -->
<section class="slide">
  <div class="abs" style="left:0;top:0;width:220px;height:180px;background:var(--navy)"></div>
  <h2 class="abs" style="left:17px;top:22px;font-family:'Abril Fatface',serif;font-weight:400;font-size:12.5px;line-height:1.22;color:#fff">Advice And<br>Counsel Throug<br>Email</h2>
  <div class="abs" style="left:10px;top:80px;width:1px;height:90px;background:var(--coral)"></div>
  <div class="abs" style="left:22px;top:82px;width:150px">
    <div style="display:flex;gap:5px;margin-bottom:12px"><span class="num" style="color:var(--coral)">1.</span><div><p style="font-family:'Abril Fatface',serif;font-size:7px;color:#fff">Lorem ipsum</p><p class="small" style="color:#fff;font-size:4.6px">Lorem ipsum dolor sit amet, consectetur adipiscing elit, sed do eiusmod tempor incididunt ut labore et dolore magna aliqua.</p></div></div>
    <div style="display:flex;gap:5px"><span class="num" style="color:var(--coral)">2.</span><div><p style="font-family:'Abril Fatface',serif;font-size:7px;color:#fff">Lorem ipsum</p><p class="small" style="color:#fff;font-size:4.6px">Lorem ipsum dolor sit amet, consectetur adipiscing elit, sed diam nonummy nibh euismod tincid</p></div></div>
  </div>
  <div class="photo" role="img" aria-label="Team meeting with laptops by a bright window" style="left:172px;top:9px;width:119px;height:163px"></div>
</section>

<!-- 7 domain -->
<section class="slide">
  <div class="side"></div>
  <h2 class="title light">A Domain ?</h2>
  <span class="url">www.pollspace.com/marareyes</span>
  <div class="photo" role="img" aria-label="Scissors cutting a red ribbon" style="left:24px;top:38px;width:116px;height:125px;background:linear-gradient(135deg,#3a3a3a,#6a2020 60%,#b3262b)"></div>
  <div class="chip" style="left:127px;top:45px;width:21px;height:8px"></div>
  <ol class="abs" style="left:160px;top:41px;list-style:none;font-family:'Abril Fatface',serif;font-size:5.6px;line-height:11.4px;color:var(--navy)">
    <li>1. It is incumbent upon us</li><li>2. In the vicinity of</li><li>3. In order to</li><li>4. In light of the fact that</li><li>5. On two different occasions</li><li>6. Conducted an interview</li><li>7. The intention of the Legislature</li><li>8. Rate of pay</li><li>9. Clearly and unequivocally satisfies</li><li>10. The order should be granted by the Court</li>
  </ol>
  <span class="pg">07</span>
</section>

<!-- 8 market -->
<section class="slide">
  <div class="side"></div>
  <h2 class="title light" style="font-size:11px">Market<br>Opportunities.</h2>
  <div class="abs tiny light" style="left:21px;top:50px;width:80px;font-size:3.9px">
    <p>Lorem ipsum dolor sit amet, consectetuer adipiscing elit, sed diam nonummy nibh euismod tincidunt ut laoreet dolore magna aliquam erat volutpat. Ut wisi enim ad minim veniam, quis nostrud exerci tation ullamcorper suscipit lobortis nisl ut aliquip ex ea commodo consequat. Duis autem vel eum iriure dolor in hendrerit i</p><br>
    <p>Lorem ipsum dolor sit amet, consectetuer adipiscing elit, sed diam nonummy nibh .</p><br>
    <p>Ut wisi enim ad minim veniam, quis nostrud exerci tation ullamcorper suscipit lobortis.</p>
  </div>
  <span class="url">www.pollspace.com/marareyes</span>
  <p class="abs" style="left:123px;top:13px;font-size:5.4px;font-weight:600;color:#222">CONSECTETUER ADIPISCING</p>
  <svg class="abs" style="left:116px;top:24px" width="196" height="110" viewBox="0 0 196 110" role="img" aria-label="Bar chart January to April">
    <g font-size="5" fill="#333" text-anchor="end">
      <text x="10" y="4">60</text><text x="10" y="17">50</text><text x="10" y="30">40</text><text x="10" y="43">30</text><text x="10" y="56">20</text><text x="10" y="69">10</text><text x="10" y="82">0</text>
    </g>
    <rect x="14" y="2" width="178" height="78" fill="none" stroke="#aaa" stroke-width=".5"/>
    <rect x="30" y="9.8" width="19" height="70.2" fill="#1d4556"/>
    <rect x="65" y="38.4" width="19" height="41.6" fill="#117a7b"/>
    <rect x="100" y="18.9" width="19" height="61.1" fill="#1d4556"/>
    <rect x="135" y="44.9" width="19" height="35.1" fill="#117a7b"/>
    <g font-size="5.2" fill="#333" text-anchor="middle"><text x="39.5" y="91">JAN</text><text x="74.5" y="91">FEB</text><text x="109.5" y="91">MAR</text><text x="144.5" y="91">APR</text></g>
  </svg>
  <div class="abs" style="left:115px;top:130px;width:90px;display:flex;gap:3px"><span style="width:5px;height:5px;border-radius:50%;background:var(--navy);margin-top:1px;flex:none"></span><div><p class="head teal">Lorem ipsum</p><p class="tiny" style="font-size:3.4px">Lorem ipsum dolor sit amet, consectetuer adipiscing elit, sed diam nonummy nibh euismod tincidunt ut laoreet</p></div></div>
  <div class="abs" style="left:212px;top:130px;width:90px;display:flex;gap:3px"><span style="width:5px;height:5px;border-radius:50%;background:var(--navy);margin-top:1px;flex:none"></span><div><p class="head teal">Lorem ipsum</p><p class="tiny" style="font-size:3.4px">Lorem ipsum dolor sit amet, consectetuer adipiscing elit, sed diam nonummy nibh euismod tincidunt ut laoreet</p></div></div>
  <span class="pg">08</span>
</section>

<!-- 9 company -->
<section class="slide">
  <h2 class="title" style="font-size:11px;line-height:1"><span style="font-size:11px">Company</span><br><span style="font-size:15px">Overview</span></h2>
  <p class="abs tiny" style="left:21px;top:47px;width:116px">Lorem ipsum dolor sit amet, consectetuer adipiscing elit, sed diam nonummy nibh euismod tincidunt ut laoreet dolore magna aliquam erat volutpat. Ut wisi enim ad minim veniam, quis nostrud exerci tation ullamcorper suscipit lobortis nisl ut aliquip ex ea commodo consequat. Duis autem vel eum iriure dolor in hendrerit i</p>
  <span class="url">www.pollspace.com/marareyes</span>
  <svg class="abs" style="left:22px;top:100px" width="116" height="64" viewBox="0 0 116 64" role="img" aria-label="Ring chart 40, 20, 20, 20 percent">
    <ellipse cx="46" cy="38" rx="44" ry="24" fill="#123441"/>
    <ellipse cx="46" cy="31" rx="44" ry="24" fill="#1d4556"/>
    <path d="M46 7a44 24 0 0 1 40 14L46 31z" fill="#117a7b"/>
    <path d="M86 21a44 24 0 0 1-10 27L46 31z" fill="#1d4556"/>
    <path d="M76 48a44 24 0 0 1-30 7L46 31z" fill="#117a7b"/>
    <ellipse cx="46" cy="31" rx="17" ry="8" fill="#fff"/>
    <g font-family="Abril Fatface,serif" fill="#fff" font-size="8"><text x="9" y="35">40%</text><text x="52" y="17">20%</text><text x="67" y="36">20%</text><text x="52" y="50">20%</text></g>
  </svg>
  <svg class="abs" style="left:146px;top:20px" width="170" height="80" viewBox="0 0 170 80" role="img" aria-label="Grouped bar chart by month">
    <g font-size="4.2" fill="#333" text-anchor="end"><text x="8" y="4">60</text><text x="8" y="14.5">50</text><text x="8" y="25">40</text><text x="8" y="35.5">30</text><text x="8" y="46">20</text><text x="8" y="56.5">10</text><text x="8" y="67">0</text></g>
    <rect x="12" y="2" width="146" height="63" fill="none" stroke="#bbb" stroke-width=".4"/>
    <rect x="20" y="23" width="3.5" height="42" fill="#1d4556"/><rect x="25" y="13" width="3.5" height="52" fill="#117a7b"/>
    <rect x="48" y="55" width="3.5" height="10" fill="#117a7b"/><rect x="53" y="29" width="3.5" height="36" fill="#1d4556"/>
    <rect x="76" y="5" width="3.5" height="60" fill="#117a7b"/><rect x="81" y="51" width="3.5" height="14" fill="#1d4556"/>
    <rect x="104" y="13" width="3.5" height="52" fill="#1d4556"/><rect x="109" y="34" width="3.5" height="31" fill="#117a7b"/>
    <g font-size="4.6" fill="#333" text-anchor="middle"><text x="24" y="74">JAN</text><text x="52" y="74">FEB</text><text x="80" y="74">MAR</text><text x="108" y="74">APR</text></g>
  </svg>
  <svg class="abs" style="left:146px;top:103px" width="170" height="64" viewBox="0 0 170 64" role="img" aria-label="Line chart across nine categories">
    <g font-size="3.8" fill="#333" text-anchor="end"><text x="8" y="3">60</text><text x="8" y="11">50</text><text x="8" y="19">40</text><text x="8" y="27">30</text><text x="8" y="35">20</text><text x="8" y="43">10</text><text x="8" y="51">0</text></g>
    <rect x="12" y="1.5" width="146" height="48" fill="none" stroke="#bbb" stroke-width=".4"/>
    <polyline points="18,41 32,49 46,31 60,10 74,26 88,15 102,29 116,31 130,26" fill="none" stroke="#1d4556" stroke-width=".8"/>
    <polyline points="18,45 32,41 46,27 60,39 74,20 88,29 102,25 116,26 130,21" fill="none" stroke="#117a7b" stroke-width=".8"/>
    <g font-size="2.8" fill="#333" text-anchor="middle"><text x="18" y="56">TEXT 01</text><text x="32" y="56">TEXT 02</text><text x="46" y="56">TEXT 03</text><text x="60" y="56">TEXT 04</text><text x="74" y="56">TEXT 05</text><text x="88" y="56">TEXT 06</text><text x="102" y="56">TEXT 07</text><text x="116" y="56">TEXT 08</text><text x="130" y="56">TEXT 09</text></g>
  </svg>
  <span class="pg">09</span>
</section>

<!-- 10 roadmap -->
<section class="slide">
  <h2 class="title" style="font-size:14px">Timeline Of Roadmap</h2>
  <span class="url">www.pollspace.com/marareyes</span>
  <svg class="abs" style="left:0;top:0" width="321" height="180" viewBox="0 0 321 180">
    <path d="M118 50C125 50 132 52 139 64C145 72 158 62 163 54M139 64C144 82 160 80 166 86M166 86C186 78 214 78 227 63M166 86C183 100 170 108 178 118C200 140 270 128 285 127" fill="none" stroke="#117a7b" stroke-width="1.2"/>
    <path d="M179 99C170 115 168 130 190 140C240 160 280 160 287 157" fill="none" stroke="#117a7b" stroke-width="1.2"/>
    <path d="M285 125v32" stroke="#1d4556" stroke-width="1" stroke-dasharray="1.5 2"/>
    <circle cx="287" cy="157" r="2" fill="#1d4556"/>
    <circle cx="285" cy="103" r="20" fill="#fff" stroke="#1d4556" stroke-width="4"/>
    <path d="M278 121l7 9 7-9z" fill="#1d4556"/>
    <text x="285" y="113" text-anchor="middle" font-size="27" font-weight="600" fill="#117a7b">1</text>
    <circle cx="179" cy="86" r="12" fill="#fff" stroke="#1d4556" stroke-width="2.5"/><text x="179" y="92" text-anchor="middle" font-size="15" font-weight="600" fill="#117a7b">2</text>
    <circle cx="227" cy="63" r="9.5" fill="#fff" stroke="#1d4556" stroke-width="2"/><text x="227" y="67.5" text-anchor="middle" font-size="12" font-weight="600" fill="#117a7b">3</text>
    <circle cx="139" cy="64" r="7" fill="#fff" stroke="#1d4556" stroke-width="1.6"/><text x="139" y="67.5" text-anchor="middle" font-size="9" font-weight="600" fill="#117a7b">4</text>
    <circle cx="163" cy="52" r="5" fill="#fff" stroke="#1d4556" stroke-width="1.2"/><text x="163" y="54.5" text-anchor="middle" font-size="6.5" font-weight="600" fill="#117a7b">5</text>
    <circle cx="118" cy="50" r="3.8" fill="#fff" stroke="#1d4556" stroke-width="1"/><text x="118" y="52" text-anchor="middle" font-size="5" font-weight="600" fill="#117a7b">6</text>
  </svg>
  <div class="abs" style="left:74px;top:48px;width:40px"><p class="head" style="font-size:4.6px">Lorem Ipsum</p><p class="tiny" style="font-size:2.6px">Lorem ipsum dolor sit amet, consectetuer adipiscing elit, sed diam nonummy nibh euismod tincid</p></div>
  <div class="abs" style="left:172px;top:40px;width:40px"><p class="head" style="font-size:4.6px">Lorem Ipsum</p><p class="tiny" style="font-size:2.6px">Lorem ipsum dolor sit amet, consectetuer adipiscing elit, sed diam nonummy nibh euismod tincid</p></div>
  <div class="abs" style="left:241px;top:46px;width:40px"><p class="head" style="font-size:4.6px">Lorem Ipsum</p><p class="tiny" style="font-size:2.6px">Lorem ipsum dolor sit amet, consectetuer adipiscing elit, sed diam nonummy nibh euismod tincid</p></div>
  <div class="abs" style="left:128px;top:92px;width:40px"><p class="head" style="font-size:4.6px">Lorem Ipsum</p><p class="tiny" style="font-size:2.6px">Lorem ipsum dolor sit amet, consectetuer adipiscing elit, sed diam nonummy nibh euismod tincid</p></div>
  <div class="abs" style="left:230px;top:111px;width:40px"><p class="head" style="font-size:4.6px">Lorem Ipsum</p><p class="tiny" style="font-size:2.6px">Lorem ipsum dolor sit amet, consectetuer adipiscing elit, sed diam nonummy nibh euismod tincid</p></div>
  <p class="abs" style="left:20px;top:115px;font-size:11px;font-weight:600;color:var(--navy)">FOR 2 YEARS</p>
  <div class="abs" style="left:20px;top:136px;display:flex;gap:4px"><span style="width:19px;height:19px;border-radius:50%;background:var(--teal);color:#fff;font-weight:700;font-size:11px;display:flex;align-items:center;justify-content:center">A</span><div><p style="font-size:8px;color:#222">2019</p><p class="tiny" style="font-size:2.6px;width:38px">Lorem ipsum dolor sit amet, consectetuer adipiscing elit, sed diam</p></div></div>
  <div class="abs" style="left:95px;top:136px;display:flex;gap:4px"><span style="width:19px;height:19px;border-radius:50%;background:var(--teal);color:#fff;font-weight:700;font-size:11px;display:flex;align-items:center;justify-content:center">B</span><div><p style="font-size:8px;color:#222">2020</p><p class="tiny" style="font-size:2.6px;width:38px">Lorem ipsum dolor sit amet, consectetuer adipiscing elit, sed diam</p></div></div>
  <span class="pg">10</span>
</section>

<!-- 11 project -->
<section class="slide">
  <h2 class="title" style="font-size:14px">Lorem Project</h2>
  <span class="url">www.pollspace.com/marareyes</span>
  <p class="abs small" style="left:19px;top:36px;width:280px;font-size:5px">Lorem ipsum dolor sit amet, consectetuer adipiscing elit, sed diam nonummy nibh euismod tincidunt ut laoreet dolore magna aliquam erat volutpat. Ut wisi enim ad minim veniam, quis nostrud exerci tation.</p>
  <p class="abs small" style="left:19px;top:61px;width:280px;font-size:5px">Lorem ipsum dolor sit amet, consectetuer adipiscing elit, sed diam nonummy nibh euismod tincidunt ut laoreet dolore magna aliquam erat volutpat. Ut wisi enim ad minim veniam.</p>
  <div class="photo" role="img" aria-label="Hand touching a glowing digital interface" style="left:25px;top:84px;width:64px;height:43px;background:linear-gradient(135deg,#12243a,#3d6fa3 50%,#c7d8ea);outline:1px solid var(--coral);outline-offset:1px"></div>
  <div class="photo" role="img" aria-label="Business people in a bright office" style="left:95px;top:84px;width:64px;height:43px;outline:1px solid var(--coral);outline-offset:1px"></div>
  <div class="photo" role="img" aria-label="Finger pressing a blue technology icon" style="left:165px;top:84px;width:64px;height:43px;background:linear-gradient(135deg,#0a1c4a,#2d6fd6 55%,#0a1c4a);outline:1px solid var(--coral);outline-offset:1px"></div>
  <div class="photo" role="img" aria-label="Network of connected digital icons" style="left:235px;top:84px;width:64px;height:43px;background:linear-gradient(135deg,#0d3550,#2e8fb0 55%,#113040);outline:1px solid var(--coral);outline-offset:1px"></div>
  <div class="abs" style="left:25px;top:131px;width:64px"><p class="head teal">Lorem ipsum</p><p class="tiny" style="font-size:3.4px">Lorem ipsum dolor sit amet, consectetuer adipiscing elit, sed diam nonummy nibh euismod tincidunt ut laoreet</p></div>
  <div class="abs" style="left:95px;top:131px;width:64px"><p class="head teal">Lorem ipsum</p><p class="tiny" style="font-size:3.4px">Lorem ipsum dolor sit amet, consectetuer adipiscing elit, sed diam nonummy nibh euismod tincidunt ut laoreet</p></div>
  <div class="abs" style="left:165px;top:131px;width:64px"><p class="head teal">Lorem ipsum</p><p class="tiny" style="font-size:3.4px">Lorem ipsum dolor sit amet, consectetuer adipiscing elit, sed diam nonummy nibh euismod tincidunt ut laoreet</p></div>
  <div class="abs" style="left:235px;top:131px;width:64px"><p class="head teal">Lorem ipsum</p><p class="tiny" style="font-size:3.4px">Lorem ipsum dolor sit amet, consectetuer adipiscing elit, sed diam nonummy nibh euismod tincidunt ut laoreet</p></div>
  <span class="pg">11</span>
</section>

<!-- 12 use cases -->
<section class="slide">
  <div class="side"></div>
  <h2 class="title light">Use Cases.</h2>
  <div class="abs tiny light" style="left:21px;top:45px;width:78px;font-size:3.9px">
    <p>Lorem ipsum dolor sit amet, consectetuer adipiscing elit, sed diam nonummy nibh euismod tincidunt ut laoreet dolore magna aliquam erat volutpat. Ut wisi enim ad minim veniam, quis nostrud exerci tation ullamcorper suscipit lobortis nisl ut aliquip ex ea commodo consequat. Duis autem vel eum iriure dolor in hendrerit i</p><br>
    <p>Lorem ipsum dolor sit amet, consectetuer adipiscing elit, sed diam nonummy nibh .</p><br>
    <p>Ut wisi enim ad minim veniam, quis nostrud exerci tation ullamcorper suscipit lobortis.</p>
  </div>
  <span class="url">www.pollspace.com/marareyes</span>
  <div class="abs" style="left:134px;top:16px;width:40px;height:74px;border:1.5px solid #222;border-radius:4px;padding:16px 4px 0"><p style="font-size:5px;color:var(--navy)">Lorem ipsum dolor</p><p class="tiny" style="font-size:2.6px;margin-top:20px">To introduce the students to the changing landscape of marketing and equip them with knowledge and tools to navigate the digital world.</p></div>
  <div class="abs" style="left:187px;top:42px;width:40px;height:88px;border:1.5px solid #222;border-radius:4px;padding:18px 4px 0"><p style="font-size:5px;color:var(--navy)">Dolor sit amet, conse</p><svg width="8" height="8" viewBox="0 0 8 8" style="display:block;margin:6px auto"><circle cx="4" cy="4" r="3" fill="none" stroke="#f26b6b" stroke-width=".7"/></svg><p class="tiny" style="font-size:2.6px;margin-top:3px">You will learn concepts and ideas in digital marketing as well as how to use different tools and strategies to optimize your digital marketing campaigns.</p></div>
  <div class="abs" style="left:240px;top:71px;width:40px;height:88px;border:1.5px solid #222;border-radius:4px;padding:18px 4px 0"><p style="font-size:5px;color:var(--navy)">Consec</p><svg width="8" height="8" viewBox="0 0 8 8" style="display:block;margin:10px auto 4px"><circle cx="4" cy="4" r="3" fill="none" stroke="#f26b6b" stroke-width=".7"/></svg><p class="tiny" style="font-size:2.6px">You are required to pass 80% of the evaluation test to obtain the certificate. The test can only be taken 3 times.</p></div>
  <span class="pg">12</span>
</section>

<!-- 13 subject -->
<section class="slide">
  <div class="side" style="width:86px"></div>
  <h2 class="title light" style="line-height:1.1">Subject<br>Title.</h2>
  <span class="url">www.pollspace.com/marareyes</span>
  <div class="photo" role="img" aria-label="Two colleagues reviewing a document" style="left:86px;top:0;width:64px;height:79px"></div>
  <div class="chip" style="left:142px;top:36px;width:16px;height:8px"></div>
  <div class="photo" role="img" aria-label="Portrait of a smiling businessman in a suit" style="left:12px;top:77px;width:66px;height:103px"></div>
  <div class="chip" style="left:72px;top:110px;width:16px;height:8px"></div>
  <div class="photo" role="img" aria-label="Two professionals talking in an office corridor" style="left:157px;top:61px;width:70px;height:109px"></div>
  <div class="chip" style="left:214px;top:147px;width:16px;height:8px"></div>
  <div class="abs" style="left:232px;top:64px;width:80px">
    <div style="display:flex;gap:3px;margin-bottom:8px"><span class="num">1.</span><div><p class="head teal">Lorem ipsum</p><p class="tiny">Lorem ipsum dolor sit amet, consectetur adipiscing elit, sed do eiusmod tempor incididunt ut labore et dolore magna aliqua. tincid</p></div></div>
    <div style="display:flex;gap:3px"><span class="num">2.</span><div><p class="head teal">Lorem ipsum</p><p class="tiny">Lorem ipsum dolor sit amet, consectetuer adipiscing elit, sed diam nonummy nibh euismod tincid</p></div></div>
  </div>
  <span class="pg">13</span>
</section>

<!-- 14 summary -->
<section class="slide">
  <div class="side"></div>
  <h2 class="title light">Summary.</h2>
  <div class="abs tiny light" style="left:21px;top:38px;width:78px;font-size:3.9px">
    <p>Lorem ipsum dolor sit amet, consectetuer adipiscing elit, sed diam nonummy nibh .</p><br>
    <p>Ut wisi enim ad minim veniam, quis nostrud exerci tation ullamcorper suscipit lobortis.</p>
  </div>
  <div class="abs" style="left:28px;top:90px;width:70px">
    <div style="display:flex;gap:3px;margin-bottom:6px"><span style="width:4px;height:4px;border-radius:50%;background:#fff;margin-top:1px;flex:none"></span><div><p style="font-size:4.5px;color:#fff">Lorem ipsum</p><p class="tiny light" style="font-size:2.6px">Lorem ipsum dolor sit amet, consectetuer adipiscing elit, sed diam nonummy nibh euismod</p></div></div>
    <div style="display:flex;gap:3px;margin-bottom:6px"><span style="width:4px;height:4px;border-radius:50%;background:#fff;margin-top:1px;flex:none"></span><div><p style="font-size:4.5px;color:#fff">Lorem ipsum</p><p class="tiny light" style="font-size:2.6px">Lorem ipsum dolor sit amet, consectetuer adipiscing elit, sed diam nonummy nibh euismod</p></div></div>
    <div style="display:flex;gap:3px"><span style="width:4px;height:4px;border-radius:50%;background:#fff;margin-top:1px;flex:none"></span><div><p style="font-size:4.5px;color:#fff">Lorem ipsum</p><p class="tiny light" style="font-size:2.6px">Lorem ipsum dolor sit amet, consectetuer adipiscing elit, sed diam nonummy nibh euismod</p></div></div>
  </div>
  <span class="url">www.pollspace.com/marareyes</span>
  <svg class="abs" style="left:110px;top:25px" width="211" height="150" viewBox="0 0 211 150">
    <path d="M133 23A55 55 0 0 0 28 56" fill="none" stroke="#1d4556" stroke-width="2.4"/>
    <path d="M22 52l6 14 6-14" fill="none" stroke="#1d4556" stroke-width="2"/>
    <path d="M28 76A55 55 0 0 0 100 129" fill="none" stroke="#1d4556" stroke-width="2.4"/>
    <path d="M100 129A55 55 0 0 0 137 60" fill="none" stroke="#1d4556" stroke-width="2.4"/>
    <circle cx="137" cy="23" r="17" fill="#1d4556"/><circle cx="137" cy="23" r="12" fill="none" stroke="#117a7b" stroke-width="4"/><circle cx="137" cy="23" r="5" fill="#fff"/>
    <circle cx="137" cy="64" r="13" fill="#1d4556"/><circle cx="137" cy="64" r="9" fill="none" stroke="#117a7b" stroke-width="3"/><circle cx="137" cy="64" r="4" fill="#fff"/>
    <circle cx="100" cy="113" r="10" fill="#1d4556"/><circle cx="100" cy="113" r="7" fill="none" stroke="#117a7b" stroke-width="2.5"/>
    <circle cx="44" cy="110" r="9" fill="#1d4556"/><circle cx="44" cy="110" r="6" fill="none" stroke="#117a7b" stroke-width="2"/>
    <circle cx="28" cy="95" r="4" fill="#1d4556"/>
    <g font-size="4.5" font-style="italic" font-weight="700" fill="#1d4556"><text x="158" y="12">85%</text><text x="106" y="65">80%</text><text x="62" y="105">50%</text><text x="113" y="130">75%</text></g>
    <path d="M151 11h6M114 63h8M55 104h6M108 126h5" stroke="#1d4556" stroke-width=".6"/>
    <g fill="#1d4556"><rect x="47" y="72" width="2" height="8"/><rect x="50" y="69" width="2" height="11"/><rect x="53" y="74" width="2" height="6"/><rect x="56" y="71" width="2" height="9"/></g>
    <text x="53" y="89" text-anchor="middle" font-size="5.5" font-weight="600" fill="#117a7b">MAIN TITLE</text>
    <text x="53" y="94" text-anchor="middle" font-size="2.6" fill="#7b8a91">Lorem ipsum dolor sit amet,</text>
    <text x="53" y="97.5" text-anchor="middle" font-size="2.6" fill="#7b8a91">consectetuer adipiscing elit</text>
    <g font-size="4.5" font-weight="600" fill="#222"><text x="163" y="30">Your Title</text><text x="163" y="74">Your Title</text><text x="0" y="116">Your Title</text><text x="130" y="114">Your Title</text></g>
    <g font-size="2.4" fill="#7b8a91"><text x="160" y="35">Lorem ipsum dolor sit amet,</text><text x="160" y="79">Lorem ipsum dolor sit amet,</text><text x="0" y="121">Lorem ipsum dolor sit amet,</text><text x="127" y="119">Lorem ipsum dolor sit amet,</text></g>
  </svg>
  <span class="pg">14</span>
</section>

<!-- 15 our timeline -->
<section class="slide">
  <h2 class="title" style="font-size:14px">Our Timeline</h2>
  <span class="url">www.pollspace.com/marareyes</span>
  <svg class="abs" style="left:0;top:0" width="321" height="180" viewBox="0 0 321 180">
    <path d="M64 40v95" stroke="#1d4556" stroke-width=".6"/><circle cx="64" cy="40" r="1.3" fill="#1d4556"/>
    <g font-size="5.4" font-weight="700" fill="#1d4556"><text x="34" y="61">2019</text><text x="34" y="85">2020</text><text x="34" y="109">2021</text></g>
    <circle cx="29" cy="59" r="2.3" fill="#1d4556"/><path d="M29 80v7M27 84a2 2 0 0 0 4 0M27.5 81h3" stroke="#1d4556" stroke-width=".8" fill="none"/><circle cx="29" cy="107" r="2.6" fill="#1d4556"/>
    <g font-size="5" fill="#fff" text-anchor="middle">
      <rect x="65" y="50" width="31" height="16" fill="#1d4556"/><text x="80" y="60">20%</text>
      <rect x="96" y="50" width="42" height="16" fill="#117a7b"/><text x="117" y="60">40%</text>
      <rect x="138" y="50" width="21" height="16" fill="#1d4556"/><text x="148" y="60">10%</text>
      <rect x="159" y="50" width="111" height="16" fill="#117a7b"/><text x="214" y="60">90%</text>
      <rect x="65" y="73" width="73" height="16" fill="#1d4556"/><text x="101" y="83">50%</text>
      <rect x="138" y="73" width="52" height="16" fill="#117a7b"/><text x="164" y="83">30%</text>
      <rect x="190" y="73" width="42" height="16" fill="#1d4556"/><text x="211" y="83">20%</text>
      <rect x="232" y="73" width="38" height="16" fill="#117a7b"/><text x="251" y="83">20%</text>
      <rect x="65" y="97" width="42" height="16" fill="#117a7b"/><text x="86" y="107">30%</text>
      <rect x="107" y="97" width="63" height="16" fill="#1d4556"/><text x="138" y="107">60%</text>
      <rect x="170" y="97" width="21" height="16" fill="#117a7b"/><text x="180" y="107">10%</text>
      <rect x="191" y="97" width="79" height="16" fill="#1d4556"/><text x="230" y="107">70%</text>
    </g>
    <g font-size="5" fill="#117a7b" text-anchor="middle"><text x="64" y="127">0%</text><text x="85" y="127">10%</text><text x="105" y="127">20%</text><text x="126" y="127">30%</text><text x="146" y="127">40%</text><text x="167" y="127">50%</text><text x="188" y="127">60%</text><text x="208" y="127">70%</text><text x="229" y="127">80%</text><text x="250" y="127">90%</text><text x="270" y="127">100%</text></g>
  </svg>
  <div class="abs" style="left:61px;top:136px;width:48px"><p style="font-size:4.5px;font-weight:600;color:var(--navy)">LOREM IPSUM</p><p class="tiny" style="font-size:2.6px">Lorem ipsum dolor sit amet, consectetuer adipiscing elit, sed diam nonummy nibh euismod tincid</p></div>
  <div class="abs" style="left:117px;top:136px;width:48px"><p style="font-size:4.5px;font-weight:600;color:var(--navy)">LOREM IPSUM</p><p class="tiny" style="font-size:2.6px">Lorem ipsum dolor sit amet, consectetuer adipiscing elit, sed diam nonummy nibh euismod tincid</p></div>
  <div class="abs" style="left:175px;top:136px;width:48px"><p style="font-size:4.5px;font-weight:600;color:var(--navy)">LOREM IPSUM</p><p class="tiny" style="font-size:2.6px">Lorem ipsum dolor sit amet, consectetuer adipiscing elit, sed diam nonummy nibh euismod tincid</p></div>
  <div class="abs" style="left:235px;top:136px;width:48px"><p style="font-size:4.5px;font-weight:600;color:var(--navy)">LOREM IPSUM</p><p class="tiny" style="font-size:2.6px">Lorem ipsum dolor sit amet, consectetuer adipiscing elit, sed diam nonummy nibh euismod tincid</p></div>
  <span class="pg">15</span>
</section>

<!-- 16 subtitle -->
<section class="slide">
  <h2 class="title" style="font-size:14px">Place subtitle text here</h2>
  <span class="url">www.pollspace.com/marareyes</span>
  <div class="photo" role="img" aria-label="Group of smiling colleagues looking at a tablet" style="left:18px;top:44px;width:285px;height:84px;background:linear-gradient(120deg,#6d5a4a,#c9b59c 45%,#7b8790)"></div>
  <div class="abs" style="left:30px;top:127px;display:flex;gap:5px;width:80px"><span style="background:var(--coral);color:#fff;font-family:'Abril Fatface',serif;font-size:9px;padding:1px 3px;height:14px;margin-top:-2px">01</span><div><p class="tiny" style="font-size:3.4px">Lorem ipsum Dolor sit amet Consectetur adipiscing</p><p class="tiny" style="font-size:3.4px;margin-top:5px">sed do eiusmod Tempor incididunt ut labore et dolore</p></div></div>
  <div class="abs" style="left:124px;top:127px;display:flex;gap:5px;width:80px"><span style="background:var(--coral);color:#fff;font-family:'Abril Fatface',serif;font-size:9px;padding:1px 3px;height:14px;margin-top:-2px">02</span><div><p class="tiny" style="font-size:3.4px">Lorem ipsum Dolor sit amet Consectetur adipiscing</p><p class="tiny" style="font-size:3.4px;margin-top:5px">sed do eiusmod Tempor incididunt ut labore et dolore</p></div></div>
  <div class="abs" style="left:217px;top:127px;display:flex;gap:5px;width:80px"><span style="background:var(--coral);color:#fff;font-family:'Abril Fatface',serif;font-size:9px;padding:1px 3px;height:14px;margin-top:-2px">03</span><div><p class="tiny" style="font-size:3.4px">Lorem ipsum Dolor sit amet Consectetur adipiscing</p><p class="tiny" style="font-size:3.4px;margin-top:5px">sed do eiusmod Tempor incididunt ut labore et dolore</p></div></div>
  <span class="pg">16</span>
</section>

<!-- 17 team -->
<section class="slide">
  <h2 class="title" style="font-size:14px">Team Members</h2>
  <span class="url">www.pollspace.com/marareyes</span>
  <p class="abs tiny" style="left:22px;top:36px;width:245px;font-size:4px">Lorem ipsum dolor sit amet, consectetuer adipiscing elit, sed diam nonummy nibh euismod tincim veniam, quis nostrud exerci tation ullamcorper suscipit lobortis nisl ut aliquip ex ea commodo consequat. Duis autem</p>
  <p class="abs tiny" style="left:22px;top:53px;width:245px;font-size:4px">Lorem ipsum dolor sit amet, cons ectetuer adipiscing elit, sed diam nonummy nibh euismod tincidunt ut laoreet dolore magna aliquam erat volutpat.</p>
  <div class="abs" style="left:0;top:89px;width:321px;height:91px;background:var(--navy)"></div>
  <div class="abs centre" style="left:38px;top:74px;width:70px">
    <div role="img" aria-label="Portrait of a team member" style="width:34px;height:34px;margin:0 auto;border-radius:50%;border:2px solid #fff;background:linear-gradient(#b8c0c4,#7d8a91)"></div>
    <p style="font-size:7px;font-weight:700;color:var(--coral);margin:4px 0 2px">OWEN HALE</p>
    <p class="tiny light" style="font-size:3.2px;color:#fff">ipsum dolor sit amet, cons ectetuer adipiscing elit, sed diam nonummy nibh euismod tincidunt ut laoreet dolore magna aliquam erat volutpat. Ut wisi enim ad minim veniam, quis nostrud</p>
  </div>
  <div class="abs centre" style="left:126px;top:74px;width:70px">
    <div role="img" aria-label="Portrait of a team member" style="width:34px;height:34px;margin:0 auto;border-radius:50%;border:2px solid #fff;background:linear-gradient(#b8c0c4,#7d8a91)"></div>
    <p style="font-size:7px;font-weight:700;color:var(--coral);margin:4px 0 2px">NORA BELL</p>
    <p class="tiny light" style="font-size:3.2px;color:#fff">ipsum dolor sit amet, cons ectetuer adipiscing elit, sed diam nonummy nibh euismod tincidunt ut laoreet dolore magna aliquam erat volutpat. Ut wisi enim ad minim veniam, quis nostrud</p>
  </div>
  <div class="abs centre" style="left:213px;top:74px;width:70px">
    <div role="img" aria-label="Portrait of a team member" style="width:34px;height:34px;margin:0 auto;border-radius:50%;border:2px solid #fff;background:linear-gradient(#b8c0c4,#7d8a91)"></div>
    <p style="font-size:7px;font-weight:700;color:var(--coral);margin:4px 0 2px">LEO GRANT</p>
    <p class="tiny light" style="font-size:3.2px;color:#fff">ipsum dolor sit amet, cons ectetuer adipiscing elit, sed diam nonummy nibh euismod tincidunt ut laoreet dolore magna aliquam erat volutpat. Ut wisi enim ad minim veniam, quis nostrud</p>
  </div>
  <span class="pg" style="color:#fff">16</span>
</section>

<!-- 18 closing -->
<section class="slide">
  <div class="abs" style="left:0;top:0;width:221px;height:180px;background:var(--navy)"></div>
  <div class="abs" style="left:221px;top:0;width:100px;height:180px;background:var(--coral)"></div>
  <h2 class="abs" style="left:22px;top:32px;font-family:'Abril Fatface',serif;font-weight:400;color:#fff;line-height:1.2"><span style="font-size:8.5px">Advice And Counsel</span><br><span style="font-size:15px">Throug <span style="color:var(--coral)">Email</span></span></h2>
  <div class="photo" role="img" aria-label="Office team gathered around a long meeting table" style="left:161px;top:22px;width:137px;height:137px"></div>
  <p class="abs" style="left:25px;top:101px;font-size:6.2px;font-weight:600;color:var(--coral)">Mara Reyes</p>
  <p class="abs" style="left:25px;top:110px;font-size:6.2px;font-weight:600;color:#fff">for Northgate Legal P.C.</p>
  <div class="abs" style="left:25px;top:126px;font-size:5.6px;color:#fff;line-height:1.5">
    <p><svg width="5" height="5" viewBox="0 0 5 5" style="vertical-align:-0.5px"><circle cx="2.5" cy="2.5" r="2.5" fill="#f26b6b"/><path d="M1.5 1.2l.6-.2.5 1-.4.3a2 2 0 0 0 .9.9l.3-.4 1 .5-.2.6C3 4.2.8 2 1.5 1.2z" fill="#fff"/></svg> 0040 721 455 902</p>
    <p><svg width="5" height="5" viewBox="0 0 5 5" style="vertical-align:-0.5px"><circle cx="2.5" cy="2.5" r="2.5" fill="#f26b6b"/><rect x="1.2" y="1.6" width="2.6" height="1.8" fill="none" stroke="#fff" stroke-width=".4"/></svg> hello.northgatelegal.com</p>
  </div>
  <p class="abs" style="left:25px;top:151px;font-size:5.4px;color:#fff">Go to <span style="color:var(--coral)">www.pollspace.com/marareyes</span></p>
  <div class="ring" style="left:147px;top:146px;width:28px;height:28px;border-color:#fff"></div>
</section>

</main>
</body>
</html>
```